Flyer-Design für Rasseclub
sehr angenehme Zusammenarbeit - tolle Vorschläge - Anregungen werden prompt umgesetzt. Vielen Dank für den schönen Flyer. Vom Drucker habe ich auch noch ein Lob erhalten. "Nicht jeder Grafiker / Designer liefere solche gute Qualität ab"
Zielgruppe
Wir sind ein Rasseclub für die Zebu-Züchter in der Schweiz. Wir setzen uns für die Interessen und die Verbreitung der Zeburinder ein. Mit unserem Flyer versuchen wir interessierten Personen einen kurzen Überblick über die Rasse zu verschaffen.
Aufgabenstellung
Wir wünschen uns einen Flyer im A4 Format, welcher 1 oder 2x gefalzt ist. Vorne und hinten Beschriftet / Gestaltet.

```html
<!DOCTYPE html>
<html lang="de">
<head>
<meta charset="utf-8">
<title>Rasseclub Zebu Auental – Flyer</title>
<link rel="stylesheet" href="https://fonts.googleapis.com/css2?family=Open+Sans:wght@300;400;600;700&display=swap">
<style>
:root{
  --bg:#dcdcdc;
  --olive:#5e6a39;
  --olive-light:#7b8450;
  --red:#e31b2a;
  --white:#ffffff;
  --ink:#2b2b2b;
}
*{box-sizing:border-box;margin:0;padding:0}
html,body{width:1200px;height:3905px;overflow:hidden}
body{background:var(--bg);font-family:"Open Sans",Arial,sans-serif;color:var(--ink);position:relative}
.sheet{position:absolute;box-shadow:0 4px 10px rgba(0,0,0,.25);overflow:hidden}
.panel{position:absolute;top:0;width:319px;height:676px;overflow:hidden}
.red-band{position:absolute;left:0;right:0;bottom:0;height:15px;background:var(--red)}
.photo{position:absolute;left:0;right:0}
.photo-zebu-single{background:linear-gradient(180deg,#8fae5a 0%,#7a9c48 60%,#a89e84 88%,#c8bfa8 100%)}
.photo-herd{background:linear-gradient(180deg,#9fae9a 0%,#b0b7a8 18%,#8fa86a 40%,#6e9040 100%)}
.logo-bar{position:absolute;left:0;right:0;top:0;height:118px;background:var(--white);display:flex;align-items:center;justify-content:center;gap:8px}
.logo-mark{width:14px;height:14px;border-radius:50%;background:var(--red)}
.logo-name{font-weight:700;font-size:17px;color:var(--red);letter-spacing:1px}
.strip{position:absolute;left:0;right:0;height:14px;background:var(--olive-light)}
.title-block{position:absolute;left:0;right:0;background:var(--olive);color:var(--white);text-align:right;padding-right:60px}
.title-small{font-weight:300;font-size:21px;margin-top:36px}
.title-big{font-weight:700;font-size:26px;letter-spacing:.5px;margin-top:2px}
.heading{font-weight:700;font-size:15px;letter-spacing:.2px;padding-bottom:12px;border-bottom:1.5px solid var(--red);width:235px;margin-bottom:18px;white-space:nowrap}
.heading-wide{font-size:14.5px;letter-spacing:0;width:255px}
.body{font-size:10.6px;line-height:1.32;font-weight:400}
.body p+p{margin-top:8px}
.olive-panel{background:var(--olive);color:var(--white)}
.olive-panel .heading{color:var(--white)}
.contact-box{position:absolute;left:32px;width:254px;height:112px;background:var(--white);color:var(--olive);font-size:10.5px;padding:18px 14px}
.text-white{position:absolute;left:0;right:0;background:var(--white);padding:34px 34px 0}
.inside{background:var(--white)}
.inside-photo{position:absolute;left:0;right:0;bottom:0;background:linear-gradient(180deg,rgba(255,255,255,1) 0%,#dfe2dc 14%,#a8b59a 30%,#86a255 48%,#6d8f3a 72%,#577a2c 100%)}
.fold-line{position:absolute;top:40px;width:1px;height:300px;background:#555}
.col{position:absolute;top:40px;width:260px}
</style>
</head>
<body>

<section class="sheet" style="left:438px;top:88px;width:321px;height:677px;">
  <div class="panel" style="left:0;width:321px;">
    <div class="logo-bar"><span class="logo-mark"></span><span class="logo-name">ZEBU AUENTAL</span></div>
    <div class="photo photo-zebu-single" style="top:118px;height:392px;" role="img" aria-label="Foto eines dunkelbraunen Zebu-Stiers auf einer Weide"></div>
    <div class="strip" style="top:510px;"></div>
    <div class="title-block" style="top:524px;height:153px;">
      <div class="title-small">Rasseclub</div>
      <div class="title-big">ZEBU AUENTAL</div>
    </div>
    <div class="red-band"></div>
  </div>
</section>

<section class="sheet" style="left:120px;top:845px;width:957px;height:676px;">
  <div class="panel" style="left:0;">
    <div class="photo photo-herd" style="top:0;height:366px;" role="img" aria-label="Foto einer gemischten Zebuherde auf der Weide"></div>
    <div class="text-white" style="top:366px;bottom:0;">
      <div class="heading">HERKUNFT</div>
      <div class="body"><p>Die Zebus (Bos indicus) gehören zu den Buckelrindern, die sich nicht nur vom Erbgut, sondern auch vom äusseren Erscheinungsbild her stark von den anderen Rinderrassen in Europa unterscheiden. Die Zebus stammen ursprünglich aus Sri Lanka und dem südlichen Kaukasus. Heute sind sie auf der ganzen Welt verbreitet. Die Zeburasse wird in 600 Rasseschläge unterteilt: vom kleinsten Zwergzebu bis zu den grössten Brahma oder Nelore. Das Wort Zebu wird vom tibetanischen Wort „zeu“ respektive. „zeba“ abgeleitet, welches übersetzt Buckel heisst.</p></div>
    </div>
  </div>
  <div class="panel olive-panel" style="left:319px;">
    <div style="padding:58px 34px 0;">
      <div class="heading">RASSECLUB</div>
      <div class="body"><p>Bei «Weiderind Verband» sind über 150 Muttertiere der Rasse Zwergzebu und Zebu registriert. Der «Rasseclub Zebu Auental» gibt es seit dem Jahr 2015. Alle, die Zebus in der Schweiz halten, sind im Rasseclub herzlich willkommen. Die Tiere können, wie jedes andere Rind auch, bei «Weiderind Verband» angemeldet werden. Selbstverständlich können auch die anerkannten Stiere im Herdebuch von «Weiderind Verband» aufgenommen werden und sind somit als Zuchttiere anerkannt.</p></div>
    </div>
    <div class="contact-box" style="top:468px;">Ihr Zebuhalter in der Nähe:</div>
  </div>
  <div class="panel" style="left:638px;">
    <div class="logo-bar"><span class="logo-mark"></span><span class="logo-name">ZEBU AUENTAL</span></div>
    <div class="photo photo-zebu-single" style="top:118px;height:392px;" role="img" aria-label="Foto eines dunkelbraunen Zebu-Stiers auf einer Weide"></div>
    <div class="strip" style="top:510px;"></div>
    <div class="title-block" style="top:524px;height:152px;">
      <div class="title-small">Rasseclub</div>
      <div class="title-big">ZEBU AUENTAL</div>
    </div>
  </div>
  <div class="red-band"></div>
</section>

<section class="sheet inside" style="left:120px;top:1588px;width:957px;height:675px;">
  <div class="inside-photo" style="top:240px;" role="img" aria-label="Foto einer Reihe brauner Zebus beim Heufressen am Zaun auf nebliger Wiese"></div>
  <div class="fold-line" style="left:319px;"></div>
  <div class="fold-line" style="left:638px;"></div>
  <div class="col" style="left:40px;">
    <div class="heading heading-wide">MERKMALE UND EIGENSCHAFTEN</div>
    <div class="body"><p>Der Buckel ist das auffälligste, äussere Merkmal der Zeburinder. Das ausgesprochen marmorierte Buckelfleisch ist eine Delikatesse. Das übrige Muskelfleisch ist sehr fettarm, mit einem leichten Wildgeschmack, feinfaserig und enthält die gesunden Omega-3-Fettsäuren.</p><p>Zum typischen Erscheinungsbild der Zebus gehören neben dem Buckel die Hörner, eine starke Wamme, ein abgezogenes und stark abgedachtes Becken, feine Extremitäten und eine schmale Stirn, die dem Kopf eine längliche Form verleiht.</p></div>
  </div>
  <div class="col" style="left:358px;">
    <div class="body"><p>Die Grösse der Tiere kann stark variieren. Die Kühe sind deutlich kleiner als die Stiere. Zebus kommen in allen Farben und Farbkombinationen vor. Auch die Hörner sind nicht immer klassisch nach oben gerichtet.</p><p>Zebus sind sehr robust und gehören zu den extensiven Rinderrassen. Die Klauenpflege kann auf ein Minimum beschränkt werden. Die Tiere sind betreffend Futter sehr genügsam. Ihnen reicht im Sommer Gras und im Winter Heu. Auf Kraftfutter und andere Zusätze, mit Ausnahme von Salz, kann verzichtet werden. Die Abkalbung ist meist leicht und geschieht ohne menschliche Hilfe. Die Mutterkühe haben einen guten Schutzinstinkt für ihre Kälber.</p></div>
  </div>
  <div class="col" style="left:673px;">
    <div class="body"><p>Während die meisten europäischen Rinderrassen unter der Sommerhitze leiden, fühlen sich Zebus bei Temperaturen um 30 Grad noch wohl. Ihr schütteres Fell und die dicke Aussenhaut schützen sie vor der Hitze. In den letzten Jahren wurde beobachtet, dass Zebusperma auch bei Temperaturen über 38°C noch befruchtungsfähig bleibt. Kalte Temperaturen sind sie sich von ihrer Heimat auch gewohnt.</p></div>
    <div class="heading" style="margin-top:30px;">EINSATZ</div>
    <div class="body"><p>Durch ihr leichtes Gewicht verursachen Zebus kaum Trittschäden, wodurch sie fast überall einsetzbar sind. Sie können auch gut zur allgemeinen Landschaftspflege eingesetzt werden.</p></div>
  </div>
  <div class="red-band"></div>
</section>

<section class="sheet" style="left:281px;top:2360px;width:638px;height:676px;">
  <div class="panel inside" style="left:0;">
    <div class="inside-photo" style="top:250px;" role="img" aria-label="Foto brauner Zebus beim Heufressen am Zaun"></div>
    <div class="col" style="left:40px;top:40px;">
      <div class="heading heading-wide">MERKMALE UND EIGENSCHAFTEN</div>
      <div class="body"><p>Der Buckel ist das auffälligste, äussere Merkmal der Zeburinder. Das ausgesprochen marmorierte Buckelfleisch ist eine Delikatesse. Das übrige Muskelfleisch ist sehr fettarm, mit einem leichten Wildgeschmack, feinfaserig und enthält die gesunden Omega-3-Fettsäuren.</p><p>Zum typischen Erscheinungsbild der Zebus gehören neben dem Buckel die Hörner, eine starke Wamme, ein abgezogenes und stark abgedachtes Becken, feine Extremitäten und eine schmale Stirn, die dem Kopf eine längliche Form verleiht.</p></div>
    </div>
  </div>
  <div class="panel" style="left:319px;">
    <div class="photo photo-herd" style="top:0;height:366px;" role="img" aria-label="Foto einer gemischten Zebuherde auf der Weide"></div>
    <div class="text-white" style="top:366px;bottom:0;">
      <div class="heading">HERKUNFT</div>
      <div class="body"><p>Die Zebus (Bos indicus) gehören zu den Buckelrindern, die sich nicht nur vom Erbgut, sondern auch vom äusseren Erscheinungsbild her stark von den anderen Rinderrassen in Europa unterscheiden. Die Zebus stammen ursprünglich aus Sri Lanka und dem südlichen Kaukasus. Heute sind sie auf der ganzen Welt verbreitet. Die Zeburasse wird in 600 Rasseschläge unterteilt: vom kleinsten Zwergzebu bis zu den grössten Brahma oder Nelore. Das Wort Zebu wird vom tibetanischen Wort „zeu“ respektive. „zeba“ abgeleitet, welches übersetzt Buckel heisst.</p></div>
    </div>
  </div>
  <div class="red-band"></div>
</section>

<section class="sheet olive-panel" style="left:438px;top:3117px;width:321px;height:675px;">
  <div style="padding:58px 34px 0;">
    <div class="heading">RASSECLUB</div>
    <div class="body"><p>Bei «Weiderind Verband» sind über 150 Muttertiere der Rasse Zwergzebu und Zebu registriert. Der «Rasseclub Zebu Auental» gibt es seit dem Jahr 2015. Alle, die Zebus in der Schweiz halten, sind im Rasseclub herzlich willkommen. Die Tiere können, wie jedes andere Rind auch, bei «Weiderind Verband» angemeldet werden. Selbstverständlich können auch die anerkannten Stiere im Herdebuch von «Weiderind Verband» aufgenommen werden und sind somit als Zuchttiere anerkannt.</p></div>
  </div>
  <div class="contact-box" style="top:468px;">Ihr Zebuhalter in der Nähe:</div>
  <div class="red-band"></div>
</section>

</body>
</html>
```